Veltaro Resident Safety and Security

Need a website for our company. Please see attached outlines and files
Main Page
Veltaro
Design – Install – Maintain
Supporting the Safety and Security needs of your Community
Best in Class Systems for the Safety and Security of your Residents and Staff
Your Trusted Advisor
Solutions
Systems tailored to the needs of your facility
Skilled Nursing Facilities
Long Term Care
CCRC’s
Assisted Living
Independent Living
Access Control
Maglocks
Keypads
Prox readers (key fob, card, etc.)
Wireless locks
Multi-Tennant
Perimeter doors
Resident Apartment doors
Nurse Call
Tone / Visual
Fixed Stations
Dome Lights
T/V+ Audio
Fixed Stations
Dome Lights
Audio communication
Wireless
Fixed Stations
Resident Pendants
Hybrid Systems
Wired and Wireless integrated for seamless notification and reporting.
CCTV
Surveillance systems to fit your security needs and your budget
Remote Access, Local or Cloud Storage
Good, Better, Best proposals
Wander management
Door Alarming
Detection of wandering resident
Remote alarming and alerts
Delay elopement to allow for redirection
Network Infrastructure
Modern infrastructure for modern systems
Conference and Telepresence
Professionally installed systems to allow for seamless clear communications between teams across infinite distances.
Our Team
Mark Dunleavy – President
Paula Hobart – Vice President of Customer Success
Colin Marsh – Account Executive
Industry Associations
Granite Harbor Guild
Massachusetts chapter of the National Guild of Care Facility Stewards
Contact Us
Phone (603) 555-0172
Email Info@Veltaro-example.com
Facilities we serve
Independent Senior Living
Assisted Living
Memory Care
CCRC (Continuing Care Retirement Community)
Skilled Nursing / Rehab
Multi-Tenant
Outpatient Surgical Centers
Endoscopy Clinics
Acute Care
Urgent Care
Commercial Properties of all types
General notes
Imagery should invoke high tech, safety, security and include healthcare themes. the circuit board shield is our logo and a ghosted image as back ground or some animation that brings in the logo or the circuit board should be incorporated.
Veltaro is a systems integration company specializing in low voltage solutions for healthcare facilities and senior living communities. The company aims to leverage its industry expertise, and innovative products to become the market leader in systems integration, focusing on enhancing safety and operational efficiency.
Vision and Mission: Veltaro’s vision is to revolutionize integrated systems within healthcare and commercial environments by delivering innovative, reliable, and tailored solutions that enhance operational efficiency and patient care. The company is committed to setting new standards for resident safety and customer satisfaction.
Company Summary: Founded by experienced industry professionals, Veltaro specializes in the design, installation, and maintenance of systems including Access Control, Nurse Call, Delayed Egress, network infrastructure, and overhead paging primarily for healthcare clients.
Products and Services: The company offers a comprehensive range of low voltage systems including Nurse Call (wired and wireless), Wander Management, Access Control, and wired/wireless network infrastructure tailored for senior living and healthcare facilities.
Mission Statement
Veltaro was founded to fill a specific need. Senor living communities and healthcare facilities of all kinds face unique challenges in regards to technology and systems integration. Veltaro is perfectly positioned with an experienced management team, skilled technicians, industry relationships with suppliers and facility management groups. We have built our reputation on excellent customer service and the highest standards of integrity. Veltaro’s vision is to revolutionize integrated systems within healthcare and commercial environments by delivering innovative, reliable, and tailored solutions that enhance operational efficiency and patient care. We are committed to setting new standards for resident safety and customer satisfaction in every project we undertake.

Target Market(s)

Senior living communities staff and management

Industry/Entity Type

Systems Intergration

Coding

Coded - Design and coding required

Font styles to use
Serif
Sans Serif

Colors
0054AA
0677BA
7BADD7
CADEEF
E8F1F8
0094D4
00A9DD
6FCCEA
C7EBF8
E9F6FB

Requirements
Must have
• unique eye catching design including circuit board (PCB) type design and our supplied logo files

```html
<!DOCTYPE html>
<html lang="en">
<head>
<meta charset="utf-8">
<title>Veltaro – Who We Serve</title>
<link rel="stylesheet" href="https://fonts.googleapis.com/css2?family=Cinzel:wght@400;500&family=Outfit:wght@400;500;600&display=swap">
<style>
:root{
  --navy:#0a2f9e;
  --deep:#0a1f7a;
  --brand:#0054AA;
  --brand-2:#0677BA;
  --sky:#0094D4;
  --cyan:#00A9DD;
  --ice:#CADEEF;
  --mist:#E8F1F8;
  --ink:#0b2a6b;
  --line:#b9cde6;
  --white:#ffffff;
}
*{box-sizing:border-box;margin:0;padding:0}
html,body{width:1200px;height:2459px;overflow:hidden}
body{position:relative;background:var(--white);font-family:"Outfit",sans-serif;color:var(--ink)}

.hero{position:absolute;left:0;top:0;width:1200px;height:497px;
  background:radial-gradient(ellipse at 75% 55%,#1a7be0 0%,#0d4fc4 35%,#0a2f9e 75%,#081f78 100%)}
.site-header{position:absolute;left:0;top:0;width:1200px;height:90px}
.brand{position:absolute;left:76px;top:22px;display:flex;align-items:center;gap:12px;color:var(--white);
  font-family:"Cinzel",serif;font-size:32px;letter-spacing:1px}
.brand-dot{width:40px;height:40px;border-radius:50%;background:var(--white)}
.main-nav{position:absolute;top:36px;left:0;font-size:13px;font-weight:600;color:var(--white);letter-spacing:.2px}
.main-nav a{position:absolute;white-space:nowrap;color:inherit;text-decoration:none}
.main-nav a.active::after{content:"";position:absolute;left:2px;right:2px;bottom:-9px;height:2px;background:var(--cyan)}
.btn-contact{position:absolute;left:1003px;top:25px;width:132px;height:37px;border-radius:19px;
  background:linear-gradient(90deg,var(--sky),var(--cyan));color:var(--white);font-size:13px;font-weight:600;
  display:flex;align-items:center;justify-content:center;text-decoration:none}
.hero-title{position:absolute;left:100px;top:212px;font-family:"Cinzel",serif;font-weight:400;font-size:54px;color:var(--white);letter-spacing:2px}
.hero-art{position:absolute;left:708px;top:105px;width:344px;height:350px;border-radius:40px 40px 172px 172px;
  background:linear-gradient(160deg,#19b8f5 0%,#0a7fe6 45%,#0b55d0 100%);opacity:.9}

.serve{position:absolute;left:0;top:497px;width:1200px;height:1529px;
  background:linear-gradient(100deg,var(--mist) 0%,rgba(232,241,248,0) 22%,rgba(232,241,248,0) 80%,var(--mist) 100%)}
.serve-mark{position:absolute;left:593px;top:76px;width:32px;height:32px;border-radius:50%;background:linear-gradient(180deg,var(--cyan),var(--brand))}
.serve-title{position:absolute;left:0;width:1200px;top:114px;text-align:center;font-family:"Cinzel",serif;font-weight:400;font-size:42px;color:var(--brand);letter-spacing:1.5px}
.serve-intro{position:absolute;left:170px;width:880px;top:190px;text-align:center;font-size:19px;line-height:30.5px;color:var(--ink)}

.cards{position:absolute;left:85px;top:329px;display:grid;grid-template-columns:repeat(3,339px);grid-auto-rows:260px;column-gap:17px;row-gap:17.5px}
.card{position:relative;background:var(--white);border:1px solid var(--line)}
.card-icon{position:absolute;left:28px;top:22px;width:70px;height:72px;border-radius:10px 10px 35px 35px;
  background:linear-gradient(160deg,var(--cyan) 0%,var(--brand) 100%)}
.card-body{position:absolute;left:109px;right:14px;top:38px}
.card-title{font-size:20px;font-weight:500;line-height:24px;color:var(--ink);margin-bottom:10px}
.card-title small{display:block;font-size:11px;font-weight:600;line-height:16px;margin-top:2px}
.card-text{font-size:13.3px;line-height:19.3px;color:var(--ink)}
.card.tall .card-body{top:26px}

.site-footer{position:absolute;left:0;top:2026px;width:1200px;height:433px;
  background:radial-gradient(ellipse at 20% 40%,#1046c0 0%,#0a36b0 50%,#082a92 100%);color:var(--white)}
.footer-brand{position:absolute;left:140px;top:72px;width:170px;text-align:center}
.footer-brand .brand-dot{width:60px;height:60px;margin:0 auto 14px}
.footer-brand span{font-family:"Cinzel",serif;font-size:31px;letter-spacing:1px}
.social{position:absolute;left:145px;top:217px;display:flex;gap:20px}
.social i{display:block;width:20px;height:20px;border-radius:50%;background:var(--white)}
.social i:first-child{width:34px;height:34px;margin:-7px 0;background:var(--cyan)}
.footer-col{position:absolute;top:92px}
.footer-col h3{font-size:19px;font-weight:600;letter-spacing:.3px;padding-bottom:8px;position:relative}
.footer-col h3::after{content:"";position:absolute;left:0;bottom:0;width:130px;height:2px;background:linear-gradient(90deg,var(--cyan),rgba(255,255,255,.7))}
.footer-col ul{list-style:none;margin-top:14px;font-size:14px;font-weight:500;line-height:21px}
.contact-list{list-style:none;margin-top:14px;font-size:14.5px;font-weight:500}
.contact-list li{display:flex;gap:12px;align-items:flex-start;margin-bottom:18px;line-height:24px}
.contact-list svg{flex:none;margin-top:3px}
.contact-list a{color:inherit}
.footer-rule{position:absolute;left:0;top:334px;width:1200px;height:1px;background:rgba(255,255,255,.18)}
.copyright{position:absolute;left:0;width:1200px;top:356px;text-align:center;font-size:14px}
</style>
</head>
<body>

<section class="hero">
  <header class="site-header">
    <div class="brand"><span class="brand-dot"></span>Veltaro</div>
    <nav class="main-nav">
      <a style="left:396px">HOME</a>
      <a style="left:477px">ABOUT US</a>
      <a style="left:587px">SOLUTIONS</a>
      <a class="active" style="left:705px">WHO WE SERVE</a>
      <a style="left:853px">LEADERSHIP TEAM</a>
    </nav>
    <a class="btn-contact">CONTACT US</a>
  </header>
  <h1 class="hero-title">WHO WE SERVE</h1>
  <div class="hero-art" role="img" aria-label="Blue shield illustration with circuit board traces"></div>
</section>

<main class="serve">
  <div class="serve-mark"></div>
  <h2 class="serve-title">WHO WE SERVE</h2>
  <p class="serve-intro">Sed ut perspiciatis unde omnis iste natus error sit voluptatem accusantium doloremque laudantium, totam rem aperiam, eaque ipsa quae ab illo inventore veritatis et quasi architecto beatae vitae dicta sunt explicabo. Nemo enim ipsam voluptatem quia t, sed quia consequuntur</p>

  <div class="cards">
    <article class="card tall"><div class="card-icon" role="img" aria-label="Independent senior living icon"></div><div class="card-body"><h3 class="card-title">Independent<br>Senior Living</h3><p class="card-text">Lorem ipsum dolor sit amet, consectetur adipiscing elit, sed do eiusmod tempor incididunt ut labore et dolore magna aliqua. Quis ipsum suspendisse ultrices gravida. Risus commodo viverra maecenas accumsan lacus vel facilisis.</p></div></article>
    <article class="card"><div class="card-icon" role="img" aria-label="Assisted living icon"></div><div class="card-body"><h3 class="card-title">Assisted Living</h3><p class="card-text">Lorem ipsum dolor sit amet, consectetur adipiscing elit, sed do eiusmod tempor incididunt ut labore et dolore magna aliqua. Quis ipsum suspendisse ultrices gravida. Risus commodo viverra maecenas accumsan lacus vel facilisis.</p></div></article>
    <article class="card"><div class="card-icon" role="img" aria-label="Memory care icon"></div><div class="card-body"><h3 class="card-title">Memory Care</h3><p class="card-text">Lorem ipsum dolor sit amet, consectetur adipiscing elit, sed do eiusmod tempor incididunt ut labore et dolore magna aliqua. Quis ipsum suspendisse ultrices gravida. Risus commodo viverra maecenas accumsan lacus vel facilisis.</p></div></article>
    <article class="card tall"><div class="card-icon" role="img" aria-label="Retirement community icon"></div><div class="card-body"><h3 class="card-title">CCRC<small>(Continuing Care Retirement Community)</small></h3><p class="card-text">Lorem ipsum dolor sit amet, consectetur adipiscing elit, sed do eiusmod tempor incididunt ut labore et dolore magna aliqua. Quis ipsum suspendisse ultrices gravida. Risus commodo viverra maecenas accumsan lacus vel facilisis.</p></div></article>
    <article class="card"><div class="card-icon" role="img" aria-label="Skilled nursing icon"></div><div class="card-body"><h3 class="card-title">Skilled Nursing / Rehab</h3><p class="card-text">Lorem ipsum dolor sit amet, consectetur adipiscing elit, sed do eiusmod tempor incididunt ut labore et dolore magna aliqua. Quis ipsum suspendisse ultrices gravida. Risus commodo viverra maecenas accumsan lacus vel facilisis.</p></div></article>
    <article class="card"><div class="card-icon" role="img" aria-label="Multi-tenant icon"></div><div class="card-body"><h3 class="card-title">Multi-Tenant</h3><p class="card-text">Lorem ipsum dolor sit amet, consectetur adipiscing elit, sed do eiusmod tempor incididunt ut labore et dolore magna aliqua. Quis ipsum suspendisse ultrices gravida. Risus commodo viverra maecenas accumsan lacus vel facilisis.</p></div></article>
    <article class="card tall"><div class="card-icon" role="img" aria-label="Outpatient surgery icon"></div><div class="card-body"><h3 class="card-title">Outpatient<br>Surgical Centers</h3><p class="card-text">Lorem ipsum dolor sit amet, consectetur adipiscing elit, sed do eiusmod tempor incididunt ut labore et dolore magna aliqua. Quis ipsum suspendisse ultrices gravida. Risus commodo viverra maecenas accumsan lacus vel facilisis.</p></div></article>
    <article class="card"><div class="card-icon" role="img" aria-label="Endoscopy clinic icon"></div><div class="card-body"><h3 class="card-title">Endoscopy Clinics</h3><p class="card-text">Lorem ipsum dolor sit amet, consectetur adipiscing elit, sed do eiusmod tempor incididunt ut labore et dolore magna aliqua. Quis ipsum suspendisse ultrices gravida. Risus commodo viverra maecenas accumsan lacus vel facilisis.</p></div></article>
    <article class="card"><div class="card-icon" role="img" aria-label="Acute care icon"></div><div class="card-body"><h3 class="card-title">Acute Care</h3><p class="card-text">Lorem ipsum dolor sit amet, consectetur adipiscing elit, sed do eiusmod tempor incididunt ut labore et dolore magna aliqua. Quis ipsum suspendisse ultrices gravida. Risus commodo viverra maecenas accumsan lacus vel facilisis.</p></div></article>
    <article class="card"><div class="card-icon" role="img" aria-label="Urgent care icon"></div><div class="card-body"><h3 class="card-title">Urgent Care</h3><p class="card-text">Lorem ipsum dolor sit amet, consectetur adipiscing elit, sed do eiusmod tempor incididunt ut labore et dolore magna aliqua. Quis ipsum suspendisse ultrices gravida. Risus commodo viverra maecenas accumsan lacus vel facilisis.</p></div></article>
    <article class="card tall"><div class="card-icon" role="img" aria-label="Commercial property icon"></div><div class="card-body"><h3 class="card-title">Commercial Properties<br>of all types</h3><p class="card-text">Lorem ipsum dolor sit amet, consectetur adipiscing elit, sed do eiusmod tempor incididunt ut labore et dolore magna aliqua. Quis ipsum suspendisse ultrices gravida. Risus commodo viverra maecenas accumsan lacus vel facilisis.</p></div></article>
  </div>
</main>

<footer class="site-footer">
  <div class="footer-brand"><div class="brand-dot"></div><span>Veltaro</span></div>
  <div class="social"><i></i><i></i><i></i><i></i></div>

  <div class="footer-col" style="left:397px">
    <h3>NAVIGATION</h3>
    <ul><li>Home</li><li>About Us</li><li>Solutions</li><li>Who we serve</li><li>Leadership Team</li><li>Contact Us</li></ul>
  </div>
  <div class="footer-col" style="left:608px">
    <h3>OUR SYSTEMS</h3>
    <ul><li>Nurse Call</li><li>Access Control</li><li>Wander Management</li><li>CCTV</li><li>Network Infrastructure</li><li>Video Conference and Telepresence</li></ul>
  </div>
  <div class="footer-col" style="left:865px">
    <h3>CONTACT US</h3>
    <ul class="contact-list">
      <li><svg width="20" height="20" viewBox="0 0 24 24" fill="#fff"><path d="M6.6 10.8a15.1 15.1 0 0 0 6.6 6.6l2.2-2.2a1 1 0 0 1 1-.25 11.4 11.4 0 0 0 3.6.57 1 1 0 0 1 1 1V20a1 1 0 0 1-1 1A17 17 0 0 1 3 4a1 1 0 0 1 1-1h3.5a1 1 0 0 1 1 1c0 1.25.2 2.45.57 3.57a1 1 0 0 1-.25 1z"/></svg>(603) 555-0172</li>
      <li><svg width="20" height="16" viewBox="0 0 24 18" fill="#fff"><path d="M2 0h20a2 2 0 0 1 2 2v14a2 2 0 0 1-2 2H2a2 2 0 0 1-2-2V2a2 2 0 0 1 2-2zm0 2v.5l10 6.5 10-6.5V2z"/></svg><a>Info@Veltaro-example.com</a></li>
      <li><svg width="16" height="20" viewBox="0 0 16 22" fill="#fff"><path d="M8 0a8 8 0 0 1 8 8c0 6-8 14-8 14S0 14 0 8a8 8 0 0 1 8-8zm0 5a3 3 0 1 0 0 6 3 3 0 0 0 0-6z"/></svg>118 Harbor Loop Suite 4<br>Dover Falls, New Hampshire 03999</li>
    </ul>
  </div>
  <div class="footer-rule"></div>
  <p class="copyright">© 2025 Veltaro LLC. All Right Reserved</p>
</footer>

</body>
</html>
```